Introduction of new dentist and new treatments

We want inform our Patients of our new dentist and new treatment methods. It is dealing about biologic dentistry and holistic dentistry. we are in switzerland and speak german

Font styles to use
Sans Serif

Colors
00a990
33b8a4
9bcb3c
acd036
cadf82
0292cd
3176b5
e34297
e667a6

Requirements
Must have
• Text, which can be edited. It will be in german
• Name of the dental clinic is
• "Brivana - Ihr Zahnarzt in Zug"
Nice to have
• A4 Layout

```html
<!DOCTYPE html>
<html lang="de">
<head>
<meta charset="utf-8">
<title>Brivana – Interdisziplinäre Zahnmedizin</title>
<link href="https://fonts.googleapis.com/css2?family=Lato:wght@400;700&family=Roboto+Slab:wght@500&display=swap" rel="stylesheet">
<style>
  :root{
    --backdrop:#e6e6e6;
    --paper:#ffffff;
    --navy:#1c2f5a;
    --blue:#2aa7e1;
    --heading-blue:#1b74bb;
    --green:#4cb74a;
    --text:#3a3a3a;
  }
  html,body{margin:0;padding:0;width:1200px;height:1200px;overflow:hidden;background:var(--backdrop);}
  .flyer{position:absolute;left:190px;top:20px;width:820px;height:1160px;background:var(--paper);overflow:hidden;}
  .hero{position:absolute;left:0;top:0;width:820px;height:467px;display:block;}
  .brand-name{font-family:"Lato",sans-serif;font-weight:400;font-size:30px;letter-spacing:6px;fill:var(--navy);}
  .brand-tagline{font-family:"Lato",sans-serif;font-weight:700;font-size:12px;fill:var(--navy);}
  .content{position:absolute;left:45px;top:452px;width:728px;}
  .section-title{font-family:"Roboto Slab",serif;font-weight:500;font-size:19px;line-height:1.3;margin:0 0 8px;text-decoration:underline;text-underline-offset:3px;text-decoration-thickness:1px;}
  .section-title .lead{color:var(--green);}
  .section-title .rest{color:var(--heading-blue);}
  .section{margin-bottom:20px;}
  .section p{font-family:"Lato",sans-serif;font-size:13.6px;line-height:18.2px;color:var(--text);margin:0 0 10px;text-align:justify;hyphens:auto;}
  .footer-line{position:absolute;left:0;width:820px;}
  .footer-green{top:1130px;height:7px;background:var(--green);}
  .footer-navy{top:1137px;height:23px;background:var(--navy);}
</style>
</head>
<body>
<div class="flyer">
  <svg class="hero" viewBox="0 0 913 520" xmlns="http://www.w3.org/2000/svg">
    <defs>
      <linearGradient id="photoTone" x1="0" y1="0" x2="1" y2="1">
        <stop offset="0" stop-color="#dfe3e6"/>
        <stop offset="0.5" stop-color="#eef0f0"/>
        <stop offset="1" stop-color="#cfd8de"/>
      </linearGradient>
    </defs>
    <rect role="img" aria-label="Foto: Zahnarzt im Gespräch mit einem älteren Patienten im Behandlungszimmer, daneben Porträt des neuen Zahnarztes" x="0" y="0" width="913" height="520" fill="url(#photoTone)"/>
    <path d="M560,520 C560,330 700,230 913,225 L913,520 Z" fill="var(--blue)"/>
    <path d="M0,530 L0,465 C60,410 150,365 250,345 L250,420 C150,410 80,440 0,500 Z" fill="var(--blue)"/>
    <path d="M0,455 C60,395 150,355 245,338" fill="none" stroke="var(--green)" stroke-width="4"/>
    <path d="M320,318 C460,325 570,435 700,465 C800,488 870,470 913,418 L913,520 L320,520 Z" fill="var(--navy)"/>
    <path d="M320,316 C460,323 570,433 700,462 C800,485 870,466 913,415" fill="none" stroke="var(--green)" stroke-width="4"/>
    <path d="M0,520 L0,478 C90,420 170,400 260,410 C420,430 560,500 700,497 C800,494 870,472 913,445 L913,520 Z" fill="var(--paper)"/>
    <circle cx="240" cy="326" r="135" fill="var(--paper)"/>
    <path d="M107,326 A133,133 0 0 1 373,326" fill="none" stroke="var(--green)" stroke-width="8"/>
    <path d="M107,326 A133,133 0 0 0 373,326" fill="none" stroke="var(--navy)" stroke-width="8"/>
    <text class="brand-name" x="240" y="366" text-anchor="middle">BRIVANA</text>
    <text class="brand-tagline" x="240" y="390" text-anchor="middle">Ihr Zahnarzt in Zug</text>
  </svg>

  <main class="content">
    <section class="section">
      <h2 class="section-title"><span class="lead">Interdisziplinäre Zahnmedizin –</span><br><span class="rest">Zusammenhang zwischen Zahnproblemen und der Gesundheit von Körper</span></h2>
      <p>Zahn und Gesundheit haben eins gemeinsam – Man vermisst sie, wenn sie fehlt. Zähne haben einen engen Zusammenhang zur Gesundheit und können diese beeinflussen. Sowohl negativ als auch positiv.</p>
    </section>
    <section class="section">
      <h2 class="section-title"><span class="lead">Funktion des Kauorgans</span> <span class="rest">und interdisziplinäre Zahnmedizin</span></h2>
      <p>„Funktion ist nicht alles. Aber ohne Funktion ist alles nichts!“ Sagte einst Prof. A. Hartmann (Zahnarzt, Gnathologie) und betonte die Bedeutung der Funktion des Kausystems.</p>
      <p>Sprechen, Kauen aber auch Körperhaltung und Stressmanagement gehören zu den Funktionen der Zähne. Ein gut funktionierendes Kauorgan (nach Prof. R. Lindner, interdisziplinäre Zahnmedizin) kann Stress bewältigen und mehr Leistung und Wohlbefinden bringen. Sehr oft erkennt man Funktionsstörungen daran, dass die Zähne nicht richtig zueinander passen oder Muskelverspannungen und Schmerzen im Kiefergelenk auftreten.</p>
    </section>
    <section class="section">
      <h2 class="section-title"><span class="lead">Zahnverlust und</span> <span class="rest">neurologische Auswirkung</span></h2>
      <p>Ein physiologisches Kausystem hat sehr feine Steuerungs- und Wahrnehmungsmöglichkeiten. Bei Zahnverlust werden diese Fähigkeiten weniger benötigt. Weniger gebrauchte Ressourcen werden von der Natur dementsprechend abgebaut. Studien zeigen, dass Menschen mit weniger Zähnen mehr Risiko zur Bildung von Demenz bergen.</p>
    </section>
    <section class="section">
      <h2 class="section-title"><span class="lead">Parodontitis und</span> <span class="rest">systemische Erkrankungen</span></h2>
      <p>Parodontitis (Entzündung des Zahnhalteapparats) ist eine der häufigsten chronischen Krankheiten weltweit und daher gut erforscht. Herzkrankheiten, Diabetes und Frühgeburtlichkeit sind einige der systemischen Krankheiten mit der Parodontitis in Zusammenhang steht. Zahnfleischbluten, Zahnlockerung, Zahnfleischschwund und Zahnverlust sind typische Begleiterscheinungen von Parodontitis. Eine systematische Parodontitis-Behandlung kann auch positive Auswirkungen auf die gesamte Gesundheit haben.</p>
    </section>
    <section class="section">
      <h2 class="section-title"><span class="lead">Ganzheitliche</span> <span class="rest">Erklärungen</span></h2>
      <p>Die komplementäre Zahnheilkunde, sehr oft auch als ganzheitliche oder biologische Zahnheilkunde bezeichnet, versucht mit Hilfe von Meridianen (Traditionelle Chinesische Medizin), den Zusammenhang zwischen Zähnen und anderen Organen und Körperteilen zu erklären. Es gibt immer mehr Patienten und Zahnärzte die von dieser Theorie und deren Ergebnissen überzeugt sind. Aufgrund der wissenschaftlichen Lage ist eine ausführliche Aufklärung vor der Behandlung sehr ratsam.</p>
    </section>
  </main>

  <div class="footer-line footer-green"></div>
  <div class="footer-line footer-navy"></div>
</div>
</body>
</html>
```